Blueprints For A Steady Home Book*

Our book is about using engineering and biblical principles to solve problems in marriage. We are the wedlock Architects. See our branded logo in the attachments. We would like to see different types of graphics that shows continuous improvement in marriage. Our colors should be Gold Black and Red. Could use white text and symbols if needed. Brief description on the back with some quotes and our Picture. Use 5.5x8.5 as the size of the book. Not sure about the spine size.

Target Market(s)

Married couples

Font styles to use
Serif

Colors

Designer to choose colors to be used in the design.

Requirements
Nice to have
• Engineering symbols and Logos.

```html
<!DOCTYPE html>
<html lang="en">
<head>
<meta charset="utf-8">
<title>Blueprints For A Steady Home — Front Cover</title>
<link rel="stylesheet" href="https://fonts.googleapis.com/css2?family=Cinzel:wght@400;500&display=swap">
<style>
  :root {
    --backdrop: #f1f1f1;
    --chalk-dark: #151515;
    --chalk-mid: #2a2a2a;
    --red: #e52328;
    --red-deep: #d21e24;
    --gold: #d9b84a;
    --gold-deep: #b8912b;
    --black: #050505;
    --white: #ffffff;
  }
  html, body {
    margin: 0;
    width: 1200px;
    height: 1108px;
    overflow: hidden;
    background: var(--backdrop);
  }
  .cover {
    position: absolute;
    left: 276px;
    top: 54px;
    width: 648px;
    height: 1000px;
    display: flex;
    flex-direction: column;
    box-shadow: 0 10px 30px rgba(0,0,0,0.18);
    font-family: "Cinzel", serif;
  }
  .chalkboard-art {
    height: 343px;
    background: radial-gradient(ellipse at 40% 40%, var(--chalk-mid), var(--chalk-dark) 75%);
  }
  .gold-rule {
    height: 6px;
    background: linear-gradient(90deg, var(--gold-deep), var(--gold), var(--gold-deep));
  }
  .title-band {
    height: 375px;
    background: linear-gradient(180deg, var(--red), var(--red-deep));
    color: var(--white);
    display: flex;
    flex-direction: column;
    align-items: center;
    justify-content: center;
    text-align: center;
    font-weight: 400;
    line-height: 1;
  }
  .title-top {
    font-size: 62px;
    letter-spacing: 1px;
    margin-bottom: 14px;
  }
  .title-joiner {
    display: flex;
    align-items: center;
    gap: 16px;
    font-size: 42px;
    width: 540px;
    margin-bottom: 8px;
  }
  .title-joiner .line {
    flex: 1;
    height: 2px;
    background: var(--white);
  }
  .title-main {
    font-size: 112px;
    letter-spacing: 2px;
  }
  .title-last {
    font-size: 100px;
    letter-spacing: 2px;
    margin-top: 4px;
  }
  .publisher-panel {
    flex: 1;
    background: var(--black);
    display: flex;
    flex-direction: column;
    align-items: center;
    justify-content: center;
    gap: 16px;
  }
  .publisher-mark {
    width: 64px;
    height: 64px;
    border-radius: 50%;
    border: 6px solid var(--gold);
    box-sizing: border-box;
  }
  .publisher-name {
    color: var(--gold);
    font-size: 34px;
    font-weight: 400;
    letter-spacing: 1px;
  }
</style>
</head>
<body>
  <main class="cover">
    <div class="chalkboard-art" role="img" aria-label="Chalkboard covered with handwritten probability formulas and bell curve graphs"></div>
    <div class="gold-rule"></div>
    <h1 class="title-band">
      <span class="title-top">BLUEPRINTS</span>
      <span class="title-joiner"><span class="line"></span>FOR A<span class="line"></span></span>
      <span class="title-main">STEADY</span>
      <span class="title-last">HOME</span>
    </h1>
    <div class="gold-rule"></div>
    <footer class="publisher-panel">
      <span class="publisher-mark"></span>
      <span class="publisher-name">the wedlock Architects</span>
    </footer>
  </main>
</body>
</html>
```